Owen Tasker Studios Business Card

Looking for a clear, modern, elegant, sharp business card that conveys a professional yet edgy image to my business as a wedding, portrait, and travel photographer. Would like something that looks vintage yet modern. Need a new business card to grow my business. We are growing the business for Wedding and Event Photography as well as fine art Photography. (Mostly Landscapes)
Updates

I’m looking through designs now but I have a new logo that i want using please.

New logo uploaded please redesign using that

PLEASE ALL DESIGNERS LOOK IN BRIEF FOR NEW LOGO

Target Market(s)

Brides, Grooms, Families with Kids, People looking for Fine Art Photography Artwork

Industry/Entity Type

Photographer

Contact Information for Business Card

Unsure

Font styles to use
Serif

Colors

Designer to choose colors to be used in the design.

Requirements
Must have
• My Website:
• http://taskerlens.examplefolio.net
• Phone:
• 323-481-5206
• Email:
• owentaskerlens@mailbox-example.net
Nice to have
• Would like a sort of shine on the printing finish.
• I like black I think it looks good on a business card.
• Can try working with my logo (png that I've attached)

```html
<!DOCTYPE html>
<html lang="en">
<head>
<meta charset="utf-8">
<title>Owen Tasker Studios – Business Card</title>
<link rel="stylesheet" href="https://fonts.googleapis.com/css2?family=Raleway:wght@300;400&display=swap">
<style>
  :root {
    --photo-deep: #1c160f;
    --photo-mid: #3a2d1f;
    --photo-warm: #5a4630;
    --photo-sky: #6f6a62;
    --band: #202020;
    --rule: #ececec;
    --ink: #f2f2f2;
  }
  * { margin: 0; padding: 0; box-sizing: border-box; }
  html, body {
    width: 1200px;
    height: 687px;
    overflow: hidden;
    background: #ffffff;
  }
  .card {
    position: relative;
    width: 1200px;
    height: 687px;
    overflow: hidden;
    font-family: "Raleway", "Helvetica Neue", Arial, sans-serif;
  }
  .card__photo {
    position: absolute;
    inset: 0;
    background:
      radial-gradient(ellipse 18% 40% at 59% 8%, var(--photo-sky) 0%, rgba(111,106,98,0) 100%),
      radial-gradient(ellipse 60% 70% at 50% 50%, var(--photo-warm) 0%, rgba(90,70,48,0) 100%),
      linear-gradient(90deg, var(--photo-mid) 0%, var(--photo-deep) 40%, var(--photo-deep) 60%, var(--photo-mid) 100%);
  }
  .card__band {
    position: absolute;
    left: 0;
    top: 242px;
    width: 1200px;
    height: 202px;
    background: var(--band);
    border-top: 12px solid var(--rule);
    border-bottom: 12px solid var(--rule);
  }
  .brand {
    position: absolute;
    left: 0;
    top: 0;
    width: 100%;
    text-align: center;
    color: var(--ink);
  }
  .brand__mark {
    position: absolute;
    left: 568px;
    top: 23px;
    width: 64px;
    height: 64px;
    border: 1.5px solid var(--ink);
  }
  .brand__name {
    position: absolute;
    left: 0;
    top: 104px;
    width: 100%;
    font-weight: 300;
    font-size: 34px;
    line-height: 1;
    letter-spacing: 0.5px;
  }
  .brand__sub {
    position: absolute;
    left: 0;
    top: 145px;
    width: 100%;
    font-weight: 400;
    font-size: 13px;
    line-height: 1;
    letter-spacing: 7px;
    padding-left: 7px;
  }
</style>
</head>
<body>
  <div class="card">
    <div class="card__photo" role="img" aria-label="Dimmed photograph of a narrow stone-paved old-town alley with a figure walking away"></div>
    <div class="card__band">
      <div class="brand">
        <span class="brand__mark" aria-hidden="true"></span>
        <p class="brand__name">OWEN TASKER</p>
        <p class="brand__sub">STUDIOS</p>
      </div>
    </div>
  </div>
</body>
</html>
```